"Rise. Shift. Thrive." Empowerment Book Cover

Hello, I need a hot, trendy, and contemporary book cover designed for my first book called "Rise. Shift. Thrive. -- 360 Bold Momentum Notes to Guide Anyone to Rise, Shift, and Thrive in Their Career & Daily Dreams."
This is my first book and I am really wanting to launch my brand with it... it would be awesome to match the inside/outside branding of the book. So we can either create the book cover to match the book guts, or update the book guts to match the cover.
Lastly, I just got a professional photoshoot done last week so we can use one of those images, or we can go with a different idea/style for the cover. The body of the book is attached. All questions welcomed, happy designing!
Target Market(s)
Gen Z, Millennials and Gen X.
Industry/Entity Type
Personal Development.
Requirements
Must have
- It must stand out and be different from other typical book covers.
Nice to have
- Success, Inspiration, Motivation, Mindset, Growth.
Should not have
- Clipart, stock art, stock look and feel.

```html
<!DOCTYPE html>
<html lang="en">
<head>
<meta charset="utf-8">
<title>Rise. Shift. Thrive. — Book Cover</title>
<link href="https://fonts.googleapis.com/css2?family=Questrial&family=Jost:wght@600&display=swap" rel="stylesheet">
<style>
  :root {
    --sky: #9ac7e1;
    --azure: #379dd7;
    --indigo: #24215a;
    --midnight: #161640;
    --ink: #0f0f24;
    --cream: #f2f1de;
    --white: #ffffff;
  }
  * { margin: 0; padding: 0; box-sizing: border-box; }
  html, body {
    width: 800px;
    height: 1200px;
    overflow: hidden;
    background: var(--ink);
  }
  .cover {
    width: 800px;
    height: 1200px;
    display: flex;
    flex-direction: column;
  }
  .band {
    display: flex;
    align-items: center;
    justify-content: center;
  }
  .band--rise   { height: 281px; background: var(--sky); }
  .band--shift  { height: 278px; background: var(--azure); }
  .band--thrive { height: 270px; background: var(--indigo); }
  .band--subtitle { height: 255px; background: var(--midnight); }
  .band--author { height: 116px; background: var(--ink); }

  .title-word {
    font-family: "Questrial", sans-serif;
    font-weight: 400;
    font-size: 196px;
    line-height: 1;
    letter-spacing: -0.035em;
    color: var(--cream);
    padding-top: 10px;
  }
  .subtitle {
    font-family: "Questrial", sans-serif;
    font-size: 33px;
    line-height: 42px;
    letter-spacing: -0.03em;
    color: var(--sky);
    text-align: center;
    padding-bottom: 8px;
  }
  .subtitle span { display: block; }
  .author {
    font-family: "Jost", sans-serif;
    font-weight: 600;
    font-size: 40px;
    letter-spacing: 0.09em;
    color: var(--white);
    padding-bottom: 8px;
  }
</style>
</head>
<body>
  <main class="cover">
    <h1 class="title" style="display:contents">
      <div class="band band--rise"><span class="title-word">Rise.</span></div>
      <div class="band band--shift"><span class="title-word">Shift.</span></div>
      <div class="band band--thrive"><span class="title-word">Thrive.</span></div>
    </h1>
    <div class="band band--subtitle">
      <p class="subtitle">
        <span>360 Bold Momentum Notes</span>
        <span>to Guide Anyone to Rise, Shift, and Thrive</span>
        <span>in Their Career &amp; Daily Dreams.</span>
      </p>
    </div>
    <div class="band band--author">
      <p class="author">Daniel Arvane</p>
    </div>
  </main>
</body>
</html>
```